I need a flyer made , the flyer can be one page or two pages or three pages . I will be posting this on Instagram and social media platforms. I am a luxury home builder , I am looking to hire a construction project manager . Below are some examples and ideas what can be on the flyer

We’re looking for a construction project manager who’s passionate about building luxury homes at the highest standards
We’re hiring construction project manager
* Experience 5+ years in residential project management with a strong portfolio of completed homes.
* location : Bergen County NJ
* excellent leadership skills, leads teams with confidence and clarity
* communicates seamlessly with architects , engineers, designers and clients
*knows how to manage budgets and timelines without compromising quality
*solves problems with a positive solution first mindset
* pays attention to every detail because in luxury the small things are the big things

Apply now , link in bio or DM to connect.

My logo is attached, my web site www.ridgelanebuilders.com
My style is modern but still warm and inviting. I like a clean classy look .
Updates

Please don’t add any images of chairs or people to the flyer , I do not want people on my flyer. Do not add standard images of offices and houses , we are luxury builders , we build homes over 2 million dollars. Keep a classy , simple modern look . High end .

You can add a white hard hat with my logo on it for a image , this is a suggestion does not have to be on my flyer ,

```html
<!DOCTYPE html>
<html lang="en">
<head>
<meta charset="utf-8">
<title>Ridgelane Builders — Construction Project Manager Hiring Flyer</title>
<link rel="stylesheet" href="https://fonts.googleapis.com/css2?family=Anton&family=Archivo:wdth,wght@62..125,400..900&family=DM+Sans:wght@400;500;700&display=swap">
<style>
  :root {
    --ink: #0e0e0e;
    --panel: #161616;
    --paper: #ffffff;
    --label: #cfcfcf;
    --speck: rgba(255,255,255,0.06);
  }
  * { margin: 0; padding: 0; box-sizing: border-box; }
  html, body {
    width: 1200px; height: 884px; overflow: hidden; background: var(--paper);
  }
  .stage {
    position: absolute; left: 0; top: 0;
    width: 2250px; height: 1658px;
    transform: scale(0.53333); transform-origin: 0 0;
  }
  .format-label {
    position: absolute;
    font-family: "Archivo", sans-serif; font-weight: 800; font-stretch: 110%;
    font-size: 46px; letter-spacing: 14px; color: var(--label);
    line-height: 1; white-space: nowrap;
  }
  .format-label--print { left: 476px; top: 20px; }
  .format-label--social { left: 1520px; top: 710px; }

  .flyer {
    position: absolute;
    background:
      radial-gradient(circle at 30% 20%, var(--speck), transparent 40%),
      radial-gradient(circle at 80% 70%, rgba(255,255,255,0.04), transparent 45%),
      radial-gradient(circle at 60% 95%, rgba(255,255,255,0.03), transparent 35%),
      var(--panel);
  }
  .flyer--print { left: 76px; top: 90px; width: 1155px; height: 1495px; }
  .flyer--social { left: 1335px; top: 777px; width: 807px; height: 808px; }

  .title-panel { position: absolute; overflow: visible; }
  .flyer--print .title-panel { left: 224px; top: 75px; width: 870px; height: 810px; }
  .flyer--social .title-panel { left: 42.5px; top: 39px; width: 458.5px; height: 427px; }

  .title-panel text { fill: var(--ink); }
  .brand-name { font-family: "DM Sans", sans-serif; font-weight: 500; }
  .headline { font-family: "Anton", sans-serif; }
  .role-title { font-family: "Archivo", sans-serif; font-weight: 800; font-stretch: 125%; fill: var(--paper) !important; }
  .location { font-family: "Archivo", sans-serif; font-weight: 700; font-stretch: 112%; }

  .intro {
    position: absolute; color: var(--paper);
    font-family: "Archivo", sans-serif; font-weight: 700; font-stretch: 110%;
    white-space: nowrap;
  }
  .flyer--print .intro {
    left: 256px; top: 893px; width: 710px;
    font-size: 29px; line-height: 41px; text-align: center;
  }
  .flyer--social .intro {
    left: 462px; top: 203px; width: 300px;
    font-size: 26px; line-height: 38.2px; text-align: left;
  }

  .requirements {
    position: absolute; background: var(--paper); color: var(--ink);
  }
  .flyer--print .requirements { left: 249px; top: 1068px; width: 686px; height: 282px; border-radius: 24px; padding: 26px 0 0 43px; }
  .flyer--social .requirements { left: 52px; top: 513px; width: 673px; height: 122px; border-radius: 14px; padding: 12px 0 0 22px; }

  .requirements h2 {
    font-family: "Archivo", sans-serif; font-weight: 800; font-stretch: 118%;
    line-height: 1; letter-spacing: 0.5px;
  }
  .flyer--print .requirements h2 { font-size: 41px; margin-bottom: 22px; }
  .flyer--social .requirements h2 { font-size: 23px; margin-bottom: 10px; }

  .requirements ul { font-family: "DM Sans", sans-serif; list-style: none; }
  .requirements li { position: relative; white-space: nowrap; }
  .requirements li::before {
    content: ""; position: absolute; border-radius: 50%; background: var(--ink);
  }
  .flyer--print .requirements ul { font-size: 20px; line-height: 31px; padding-left: 33px; }
  .flyer--print .requirements li::before { width: 5px; height: 5px; left: -22px; top: 14px; }
  .flyer--social .requirements ul {
    font-size: 11.3px; line-height: 17px; padding-left: 21px; font-weight: 500;
    display: grid; grid-template-columns: 312px 320px; grid-auto-flow: column; grid-template-rows: repeat(3, 17px);
  }
  .flyer--social .requirements li::before { width: 3.5px; height: 3.5px; left: -12px; top: 7px; }

  .announce { position: absolute; }
  .flyer--print .announce { left: 788px; top: 1022px; width: 176px; height: 176px; }
  .flyer--social .announce { left: 677px; top: 475px; width: 80px; height: 80px; }

  .apply {
    position: absolute; display: flex; background: var(--paper); border-radius: 18px; padding: 4px;
  }
  .flyer--print .apply { left: 249px; top: 1368px; width: 683px; height: 72px; }
  .flyer--social .apply { left: 52px; top: 679px; width: 673px; height: 72px; border-radius: 14px; }
  .apply-label {
    display: flex; align-items: center; justify-content: center;
    font-family: "Archivo", sans-serif; font-weight: 700; font-stretch: 112%;
    font-size: 31px; color: var(--ink);
  }
  .flyer--print .apply-label { width: 303px; }
  .flyer--social .apply-label { width: 299px; }
  .apply-contact {
    flex: 1; background: var(--ink); color: var(--paper); border-radius: 4px 14px 14px 4px;
    display: flex; flex-direction: column; justify-content: center; align-items: center;
    font-family: "Archivo", sans-serif; font-size: 21.5px; line-height: 26px; font-weight: 400;
  }
  .apply-contact strong { font-weight: 600; }
</style>
</head>
<body>
<div class="stage">

  <div class="format-label format-label--print">PRINT SIZE</div>
  <div class="format-label format-label--social">SOCIAL MEDIA</div>

  <section class="flyer flyer--print">
    <svg class="title-panel" viewBox="300 165 870 810">
      <rect role="img" aria-label="Brand house emblem area" x="320" y="172" width="702" height="798" fill="#fff"/>
      <text class="brand-name" x="671" y="300" font-size="56" text-anchor="middle" letter-spacing="3">RIDGELANE</text>
      <text class="brand-name" x="671" y="352" font-size="30" text-anchor="middle" letter-spacing="6">builders</text>
      <text class="headline" x="370" y="598" font-size="200" textLength="590" lengthAdjust="spacingAndGlyphs">WE ARE</text>
      <text class="headline" x="400" y="805" font-size="200" textLength="530" lengthAdjust="spacingAndGlyphs">HIRING</text>
      <rect x="381" y="818" width="574" height="90" fill="#0e0e0e"/>
      <text class="role-title" x="470" y="858" font-size="38" textLength="396" lengthAdjust="spacingAndGlyphs">CONSTRUCTION</text>
      <text class="role-title" x="423" y="896" font-size="38" textLength="490" lengthAdjust="spacingAndGlyphs">PROJECT MANAGER</text>
      <text class="location" x="395" y="950" font-size="48" textLength="547" lengthAdjust="spacingAndGlyphs">Bergen County, NJ</text>
    </svg>

    <p class="intro">We’re looking for a Residential Project<br>Manager with 5+ years experience and a<br>strong portfolio of completed homes.</p>

    <div class="requirements">
      <h2>REQUIREMENTS:</h2>
      <ul>
        <li>Lead teams with confidence</li>
        <li>Coordinate engineers &amp; trades</li>
        <li>Communicate with architects, designers &amp; clients</li>
        <li>Manage budgets &amp; timelines without sacrificing quality</li>
        <li>Solve problems with a solution-first mindset</li>
        <li>Obsess over the details — in luxury, they matter most</li>
      </ul>
    </div>

    <svg class="announce" viewBox="0 0 100 100" aria-hidden="true">
      <circle cx="50" cy="50" r="49" fill="#fff" stroke="#0e0e0e" stroke-width="0.6"/>
      <circle cx="50" cy="50" r="40" fill="#0e0e0e"/>
      <g fill="#fff" stroke="#fff" stroke-linecap="round">
        <polygon points="36,58 50,34 66,60" stroke-width="2" stroke-linejoin="round"/>
        <circle cx="63" cy="58" r="5" stroke="none"/>
        <line x1="53" y1="60" x2="49" y2="71" stroke-width="2.2"/>
        <line x1="38" y1="33" x2="41" y2="38" stroke-width="1.8"/>
        <line x1="30" y1="44" x2="35" y2="46" stroke-width="1.8"/>
        <line x1="28" y1="57" x2="33" y2="55" stroke-width="1.8"/>
      </g>
    </svg>

    <div class="apply">
      <div class="apply-label">Apply Now</div>
      <div class="apply-contact">
        <span>Link in bio or DM to connect.</span>
        <strong>info@ridgelanebuilders.com</strong>
      </div>
    </div>
  </section>

  <section class="flyer flyer--social">
    <svg class="title-panel" viewBox="300 165 870 810">
      <rect role="img" aria-label="Brand house emblem area" x="320" y="172" width="702" height="798" fill="#fff"/>
      <text class="brand-name" x="671" y="300" font-size="56" text-anchor="middle" letter-spacing="3">RIDGELANE</text>
      <text class="brand-name" x="671" y="352" font-size="30" text-anchor="middle" letter-spacing="6">builders</text>
      <text class="headline" x="370" y="598" font-size="200" textLength="590" lengthAdjust="spacingAndGlyphs">WE ARE</text>
      <text class="headline" x="400" y="805" font-size="200" textLength="530" lengthAdjust="spacingAndGlyphs">HIRING</text>
      <rect x="381" y="818" width="574" height="90" fill="#0e0e0e"/>
      <text class="role-title" x="470" y="858" font-size="38" textLength="396" lengthAdjust="spacingAndGlyphs">CONSTRUCTION</text>
      <text class="role-title" x="423" y="896" font-size="38" textLength="490" lengthAdjust="spacingAndGlyphs">PROJECT MANAGER</text>
      <text class="location" x="395" y="950" font-size="48" textLength="547" lengthAdjust="spacingAndGlyphs">Bergen County, NJ</text>
    </svg>

    <p class="intro">We’re looking for a<br>Residential Project<br>Manager with 5+<br>years experience<br>and a strong<br>portfolio of<br>completed homes.</p>

    <div class="requirements">
      <h2>REQUIREMENTS:</h2>
      <ul>
        <li>Lead teams with confidence</li>
        <li>Coordinate engineers &amp; trades</li>
        <li>Communicate with architects, designers &amp; clients</li>
        <li>Manage budgets &amp; timelines without sacrificing quality</li>
        <li>Solve problems with a solution-first mindset</li>
        <li>Obsess over the details — in luxury, they matter most</li>
      </ul>
    </div>

    <svg class="announce" viewBox="0 0 100 100" aria-hidden="true">
      <circle cx="50" cy="50" r="49" fill="#fff" stroke="#0e0e0e" stroke-width="0.6"/>
      <circle cx="50" cy="50" r="40" fill="#0e0e0e"/>
      <g fill="#fff" stroke="#fff" stroke-linecap="round">
        <polygon points="36,58 50,34 66,60" stroke-width="2" stroke-linejoin="round"/>
        <circle cx="63" cy="58" r="5" stroke="none"/>
        <line x1="53" y1="60" x2="49" y2="71" stroke-width="2.2"/>
        <line x1="38" y1="33" x2="41" y2="38" stroke-width="1.8"/>
        <line x1="30" y1="44" x2="35" y2="46" stroke-width="1.8"/>
        <line x1="28" y1="57" x2="33" y2="55" stroke-width="1.8"/>
      </g>
    </svg>

    <div class="apply">
      <div class="apply-label">Apply Now</div>
      <div class="apply-contact">
        <span>Link in bio or DM to connect.</span>
        <strong>info@ridgelanebuilders.com</strong>
      </div>
    </div>
  </section>

</div>
</body>
</html>
```